Business Card for Web Design consulting firm

Business card designs for Web Design consulting firm

Target Market(s)

English speaking adults ages 30 - 60. Predominantly professional services eg. Doctor, Dentist

Industry/Entity Type

Consulting

Requirements
Must have
• Double sided card

```html
<!DOCTYPE html>
<html lang="en">
<head>
<meta charset="utf-8">
<title>Korvela business card</title>
<link rel="stylesheet" href="https://fonts.googleapis.com/css2?family=Noto+Sans:wght@400&display=swap">
<style>
  :root {
    --card-black: #000000;
    --card-orange: #f7931e;
    --ink-white: #ffffff;
    --ink-black: #000000;
    --page: #ffffff;
  }
  html, body {
    margin: 0;
    padding: 0;
    width: 1200px;
    height: 361px;
    overflow: hidden;
    background: var(--page);
  }
  .sheet {
    position: relative;
    width: 1200px;
    height: 361px;
    font-family: "Noto Sans", Arial, sans-serif;
  }
  .card {
    position: absolute;
    overflow: hidden;
    border-radius: 30px;
  }
  .card--front {
    left: 0;
    top: 0;
    width: 592px;
    height: 356px;
    background: var(--card-black);
  }
  .card--back {
    left: 610px;
    top: 6px;
    width: 590px;
    height: 355px;
    background: var(--card-orange);
  }
  .ribbon-art {
    position: absolute;
    display: block;
  }
  .ribbon-art--front {
    left: 0;
    top: 76px;
    width: 592px;
    height: 244px;
  }
  .ribbon-art--back {
    left: 0;
    top: 42px;
    width: 168px;
    height: 272px;
  }
  .brand-name {
    position: absolute;
    margin: 0;
    font-weight: 400;
    text-transform: uppercase;
    line-height: 1;
    white-space: nowrap;
  }
  .brand-name--front {
    left: 30px;
    top: 44px;
    font-size: 24px;
    letter-spacing: 7px;
    color: var(--ink-white);
  }
  .brand-name--back {
    right: 58px;
    top: 272px;
    font-size: 52px;
    letter-spacing: 14px;
    margin-right: -14px;
    color: var(--ink-black);
  }
  .contact {
    position: absolute;
    right: 62px;
    top: 60px;
    margin: 0;
    text-align: right;
    font-style: normal;
    font-size: 16px;
    line-height: 20px;
    color: var(--ink-white);
  }
  .contact__line {
    display: block;
  }
  .contact__group {
    display: block;
    margin-top: 7px;
  }
  .contact__group--web {
    margin-top: 8px;
  }
  .contact__label {
    color: var(--ink-black);
  }
</style>
</head>
<body>
<main class="sheet">
  <section class="card card--front" aria-label="Card front">
    <svg class="ribbon-art ribbon-art--front" role="img" aria-label="Flowing orange and white ribbon bands sweeping across the card" viewBox="0 0 592 244" preserveAspectRatio="none">
      <defs>
        <linearGradient id="front-ribbon-tone" x1="0" y1="0" x2="1" y2="0">
          <stop offset="0" stop-color="#f7931e"/>
          <stop offset="0.35" stop-color="#f6e4cc"/>
          <stop offset="0.65" stop-color="#f7931e"/>
          <stop offset="1" stop-color="#2a1a08"/>
        </linearGradient>
      </defs>
      <rect x="0" y="0" width="592" height="244" fill="url(#front-ribbon-tone)" opacity="0.9"/>
    </svg>
    <p class="brand-name brand-name--front">Korvela</p>
  </section>

  <section class="card card--back" aria-label="Card back">
    <svg class="ribbon-art ribbon-art--back" role="img" aria-label="White ribbon band sweeping down and up across the card" viewBox="0 0 168 272" preserveAspectRatio="none">
      <defs>
        <linearGradient id="back-ribbon-tone" x1="0" y1="0" x2="1" y2="1">
          <stop offset="0" stop-color="#ffffff"/>
          <stop offset="1" stop-color="#fbc98a"/>
        </linearGradient>
      </defs>
      <rect x="0" y="0" width="168" height="272" fill="url(#back-ribbon-tone)" opacity="0.75"/>
    </svg>

    <address class="contact">
      <span class="contact__line">p.o. box&nbsp; 2817</span>
      <span class="contact__line">west harbourne</span>
      <span class="contact__line">queensland 4519</span>
      <span class="contact__group">
        <span class="contact__line"><span class="contact__label">p|</span>07 5550 1234</span>
        <span class="contact__line"><span class="contact__label">m|</span>0491 570 156</span>
      </span>
      <span class="contact__group contact__group--web">
        <span class="contact__line"><span class="contact__label">e|</span> info@korvela.com</span>
        <span class="contact__line"><span class="contact__label">w|</span> www.korvela.com</span>
      </span>
    </address>

    <p class="brand-name brand-name--back">Korvela</p>
  </section>
</main>
</body>
</html>
```